Clearview Property Inspections

Property Inspection ( pre-purchase building inspections, swimming pool inspection, pest inspection , maintenance)

Industry/Entity Type

Building

Contact Information for Business Card

Tomas Varnell
info@clearviewinspect-demo.com.au
0412 867 219

ClearView Property Inspections
www.clearviewinspect-demo.com.au

on the back

Property Inspections
Property Maintenance

Safe Home....Safe Familu

```html
<!DOCTYPE html>
<html lang="en">
<head>
<meta charset="utf-8">
<title>ClearView Property Inspections – Business Card</title>
<link href="https://fonts.googleapis.com/css2?family=Hind:wght@400;600;700&family=Courgette&display=swap" rel="stylesheet">
<style>
  :root {
    --stage: #000000;
    --yellow: #fff200;
    --ink: #1b1b1f;
    --navy-deep: #22325f;
    --navy: #2a4a8c;
    --sky: #2f86c9;
    --gold: #f5e53a;
    --white: #ffffff;
  }
  * { margin: 0; padding: 0; box-sizing: border-box; }
  html, body {
    width: 1200px; height: 1000px; overflow: hidden;
    background: var(--stage);
  }
  .stage { position: relative; width: 1200px; height: 1000px; }

  .card {
    position: absolute; left: 220px; width: 763px; height: 460px; overflow: hidden;
  }
  .card svg.swoosh { position: absolute; inset: 0; width: 763px; height: 460px; }

  /* Front */
  .card--front { top: 35px; background: var(--yellow); color: var(--ink); }
  .brand {
    position: absolute; left: 62px; top: 150px; width: 240px; text-align: center;
  }
  .brand__mark {
    display: inline-block; width: 16px; height: 16px; background: var(--ink);
    margin-bottom: 12px;
  }
  .brand__name {
    font-family: "Hind", sans-serif; font-weight: 700; font-size: 24px;
    line-height: 1.2; color: var(--ink);
  }
  .divider {
    position: absolute; left: 332px; top: 123px; width: 2px; height: 150px;
    background: var(--ink);
  }
  .contact {
    position: absolute; left: 375px; top: 122px;
    font-family: "Hind", sans-serif; font-size: 21px; line-height: 27px;
  }
  .contact__name { font-weight: 700; font-size: 23px; margin-bottom: 26px; }
  .contact__company { font-weight: 700; }

  /* Back */
  .card--back {
    top: 512px;
    background:
      radial-gradient(ellipse 420px 300px at 470px 210px, var(--sky) 0%, var(--navy) 55%, var(--navy-deep) 100%);
  }
  .service {
    position: absolute; top: 26px;
    font-family: "Courgette", cursive; font-size: 27px; letter-spacing: 1px; color: var(--gold);
  }
  .service--inspections { left: 36px; }
  .service--maintenance { left: 430px; }
  .back-tagline {
    position: absolute; left: 0; right: 0; top: 382px; text-align: center;
    font-family: "Hind", sans-serif; font-weight: 600; font-size: 42px; color: var(--gold);
    letter-spacing: 1px;
  }
</style>
</head>
<body>
<div class="stage">

  <section class="card card--front">
    <svg class="swoosh" viewBox="0 0 763 460" aria-hidden="true">
      <path d="M0 322 C300 318 550 340 705 385 C550 362 300 350 0 352 Z" fill="var(--white)"/>
    </svg>
    <div class="brand">
      <span class="brand__mark"></span>
      <div class="brand__name">Clearview<br>Property Inspections</div>
    </div>
    <div class="divider"></div>
    <div class="contact">
      <div class="contact__name">Tomas Varnell</div>
      <div class="contact__email">info@clearviewinspect-demo.com.au</div>
      <div class="contact__phone">0412 867 219</div>
      <div class="contact__company">ClearView Property Inspections</div>
      <div class="contact__web">www.clearviewinspect-demo.com.au</div>
    </div>
  </section>

  <section class="card card--back">
    <svg class="swoosh" viewBox="0 0 763 460" aria-hidden="true">
      <path d="M20 385 C200 342 500 326 763 323 L763 350 C500 350 250 360 20 385 Z" fill="var(--white)"/>
    </svg>
    <div class="service service--inspections">Property Inspections</div>
    <div class="service service--maintenance">Property Maintenance</div>
    <div class="back-tagline">Clear View...Sound Home</div>
  </section>

</div>
</body>
</html>
```